Corvane Power Holdings Website

We have color scheme, logo and content, but need a design options in PDF format for the website. The PDF should guide us in how to use the color scheme and fonts in the site design (what background colors to use where, what link and hover colors to you, when to use which fonts...)

Corvane Power Holdings wants a conservative and straightforward website design that is in line with the banking industry. At the same time, Corvane wants the design to be innovative and cutting-edge in line with the renewable energy industry. Overall, the site design must be present the company as professional, serious, knowledgeable, experienced, reliable, and successful as well as a global good citizen.
Updates

We are closing this project. Thank you all for your beautiful work. Our designer was sick, but informed us today that she is better and able to resume her work. So we are closing this project and restarting work with her. Wish you all health and success.

Target Market(s)

investors, partners, developers, investment community, private equity community

Industry/Entity Type

Investment

Number of Pages Required

2 page

Requirements
Must have
• The color scheme is attached.
The logo is attached.
Fonts are Questrial and Cormorant (as used in logo).
The site must use these colors and fonts and logo design.

The 2 pages we need designed are the homepage and the portfolio page.
Homepage - The portfolio map on the homepage will be an image like with hotspots that link to portfolio items. This map image might go well with logo:
https://www.pictavo-stock.example/abstract-polygon-world-map-vector-illustration-geometric-structure-in-blue-color-for-presentation-booklet-website-and-other-design-projects-pol-image552093418.html
But we would need to zoom in on Israel and EU, and leave out US / Asia-Pacific.
The way the map will work technically (using hotspots) should be something like:
https://brindlepower.example.il/geographic-spread/.
Portfolio Page - The portfolio map there will be a Google Map/
Nice to have
• The content for the site is attached as a Word Doc, and much of it is in place at http://corvanefund.example.host4821.sample-server.example/. The design must fit this content, but we are open to some layout changes.
Design Requests:
• nav bar – light animation like https://pellucovet.example/ and https://www.tq-residencylaw.example/
• innovative, unique design with welcoming, appealing, modern feel
• engaging content display by using parallax and subtle movement
• clean, intuitive, easy to navigation layout

```html
<!DOCTYPE html>
<html lang="en">
<head>
<meta charset="utf-8">
<title>Corvane Power Holdings</title>
<link rel="stylesheet" href="https://fonts.googleapis.com/css2?family=Cormorant+Garamond:wght@500;600&family=Questrial&display=swap">
<style>
:root{
  --green:#76cc1e;
  --blue:#5aa3dc;
  --deep:#0f3b2e;
  --heading:#1b4a33;
  --text:#3d3d3d;
  --white:#ffffff;
  --yellow:#f4d63a;
}
*{box-sizing:border-box;margin:0;padding:0}
html,body{width:1200px;height:2693px;overflow:hidden}
body{position:relative;font-family:'Questrial',sans-serif;color:var(--text);background:var(--white)}
.abs{position:absolute}
.serif{font-family:'Cormorant Garamond',serif;font-weight:600;text-transform:uppercase;letter-spacing:.5px}

.hero{left:0;top:0;width:1200px;height:695px;background:linear-gradient(180deg,#5f7370 0%,#8c9a97 30%,#4f6b55 55%,#3f6a34 75%,#6c6a55 100%)}
.brand{left:112px;top:38px;display:flex;align-items:center;gap:12px;color:var(--white)}
.brand-dot{width:46px;height:46px;border-radius:50%;background:var(--green)}
.brand-name{font-family:'Questrial',sans-serif;font-size:30px;line-height:1}
.nav{right:113px;top:52px;display:flex;gap:33px;font-size:14.5px;color:var(--white)}
.nav .active{color:var(--green)}
.hero-box{left:291px;top:261px;width:618px;height:162px;background:rgba(40,70,55,.55);text-align:center;color:var(--white);padding-top:27px}
.hero-box h1{font-size:43px;line-height:1.1}
.hero-box p{font-size:18px;line-height:28px;margin:22px auto 0;width:540px}

.stats{left:112px;top:627px;width:975px;height:169px;display:flex;gap:1px}
.stat{flex:1;color:var(--white);text-align:center;padding-top:46px}
.stat.g{background:var(--green)}.stat.b{background:var(--blue)}
.stat b{display:block;font-weight:400;font-size:32px;line-height:1}
.stat span{display:block;font-size:16.5px;line-height:26px;margin-top:16px}

.h2{color:var(--heading);font-size:35px;line-height:38px}
.body-copy{font-size:15px;line-height:28px}
.btn{display:inline-flex;align-items:center;gap:7px;border-radius:27px;font-size:14.5px;height:52px;padding:0 25px;color:var(--white)}
.btn.grad{background:linear-gradient(90deg,var(--blue),var(--green))}
.btn.outline{border:2px solid currentColor;height:50px}
.arrow{width:14px;height:14px}

.strategy-text{left:110px;top:930px;width:492px}
.strategy-text p{margin-top:28px;text-align:justify}
.strategy-text .btn{margin-top:36px}
.strategy-photo{left:662px;top:905px;width:425px;height:349px;background:linear-gradient(160deg,#1b2fa0 0%,#2a47b8 35%,#9aa59a 60%,#6d7440 100%)}

.band-left{left:0;top:1363px;width:601px;height:383px;background:linear-gradient(90deg,#f2b43c 0%,#e6d43a 50%,#d0e832 100%);padding:70px 0 0 110px;color:#2b2b1a}
.band-right{left:601px;top:1363px;width:599px;height:383px;background:linear-gradient(90deg,#4e9fd8 0%,#6fb7b0 55%,#9ad64a 100%);padding:70px 0 0 42px;color:var(--white)}
.band-left .h2,.band-right .h2{font-size:31px;line-height:42px}
.band-left .h2{color:var(--heading)}
.band-right .h2{color:var(--white)}
.band-left p,.band-right p{font-size:15px;line-height:26px;margin-top:26px;width:430px}
.band-left .btn,.band-right .btn{margin-top:35px}

.map{left:110px;top:1858px;width:426px;height:349px;background:linear-gradient(120deg,#3fa86b 0%,#9bc93a 30%,#f3b52e 60%,#f39a2a 100%);box-shadow:0 6px 18px rgba(0,0,0,.12)}
.powering{left:596px;top:1906px;width:492px}
.powering p{margin-top:30px}
.powering .btn{margin-top:36px}

.footer{left:0;top:2317px;width:1200px;height:376px;background:var(--deep);color:var(--white)}
.contact{top:66px;width:260px;text-align:center}
.contact .ring{width:78px;height:78px;border-radius:50%;border:2px solid var(--white);margin:0 auto;display:flex;align-items:center;justify-content:center}
.contact .ring.fill{background:#1e6aa8;border-color:#1e6aa8}
.contact h3{font-size:17px;font-weight:700;font-family:'Questrial',sans-serif;margin-top:20px;letter-spacing:.3px}
.contact p{font-size:12.5px;line-height:21px;margin-top:12px}
.foot-bar{left:0;top:320px;width:1200px;height:40px;font-size:13px;display:flex;align-items:center}
.studio{position:absolute;left:112px;display:flex;align-items:center;gap:10px}
.studio i{width:36px;height:36px;border-radius:50%;background:var(--green);display:block}
.legal{position:absolute;left:324px}
.to-top{position:absolute;right:113px;display:flex;align-items:center;gap:12px}
.to-top i{width:36px;height:36px;border-radius:50%;background:var(--green);display:flex;align-items:center;justify-content:center}
</style>
</head>
<body>

<header class="hero abs" role="img" aria-label="Aerial photo of a renewable energy plant among green hills with wind turbines under a cloudy sky">
  <div class="brand abs"><span class="brand-dot"></span><span class="brand-name">Corvane</span></div>
  <nav class="nav abs">
    <span class="active">HOME</span><span>ABOUT</span><span>STRATEGY</span><span>PORTFOLIO</span><span>CONTACT</span>
  </nav>
  <div class="hero-box abs">
    <h1 class="serif">Illuminating the Future</h1>
    <p>Investing in clean energy to generate sustainable returns for our investors and planet</p>
  </div>
</header>

<section class="stats abs">
  <div class="stat g"><b>10</b><span>Years of Operation</span></div>
  <div class="stat b"><b>6</b><span>Countries of Investments</span></div>
  <div class="stat g"><b>600</b><span>MW under Management</span></div>
  <div class="stat b"><b>€500,000,000</b><span>Assets under<br>Management</span></div>
</section>

<section class="strategy-text abs">
  <h2 class="h2 serif">Proven Investment<br>Strategy</h2>
  <p class="body-copy">Achieving consistently high annualized returns and capital gains by leveraging our energy sector experience, broadgeographic footprint, dedicated local networks, value creation and implementation of platform structures</p>
  <a class="btn grad">OUR APPROACH <svg class="arrow" viewBox="0 0 16 16"><circle cx="8" cy="8" r="8" fill="#fff"/><path d="M5 8h6M8.5 5l3 3-3 3" stroke="#6fb6b0" stroke-width="2" fill="none"/></svg></a>
</section>
<div class="strategy-photo abs" role="img" aria-label="Photo of a modern power plant building with curved green facades under a deep blue sky"></div>

<section class="band-left abs" role="img" aria-label="Industrial energy facility photo tinted in a yellow to lime gradient">
  <h2 class="h2 serif">Expertise. Resourcefulness.<br>Integrity.</h2>
  <p>Funding clean energy projects that maximise value to our investors and contribute to a more sustainable world</p>
  <a class="btn outline" style="color:#1a1a1a">ABOUT US <svg class="arrow" viewBox="0 0 16 16"><circle cx="8" cy="8" r="8" fill="#1a1a1a"/><path d="M5 8h6M8.5 5l3 3-3 3" stroke="#e0d63a" stroke-width="2" fill="none"/></svg></a>
</section>
<section class="band-right abs" role="img" aria-label="Aerial energy plant photo tinted in a blue to green gradient">
  <h2 class="h2 serif">Hands-on Investment<br>Management</h2>
  <p>Utilising our multi-disciplinary knowledge, sectorexpertise, extensive experience and collaborative spirit</p>
  <a class="btn outline">OUR TEAM <svg class="arrow" viewBox="0 0 16 16"><circle cx="8" cy="8" r="8" fill="#fff"/><path d="M5 8h6M8.5 5l3 3-3 3" stroke="#6cb0c0" stroke-width="2" fill="none"/></svg></a>
</section>

<div class="map abs" role="img" aria-label="Polygon-style map of Europe, Africa and Asia with portfolio location markers"></div>
<section class="powering abs">
  <h2 class="h2 serif">Powering the UK</h2>
  <p class="body-copy">Corvane’ energy funds provide a diversified portfolio of assets- in operation and under construction, in multiple markets -that drive high investment returns and a balanced risk profile.</p>
  <a class="btn grad">FIND NOW <svg class="arrow" viewBox="0 0 16 16"><circle cx="8" cy="8" r="8" fill="#fff"/><path d="M5 8h6M8.5 5l3 3-3 3" stroke="#6fb6b0" stroke-width="2" fill="none"/></svg></a>
</section>

<footer class="footer abs">
  <div class="contact abs" style="left:103px">
    <div class="ring fill"><svg width="22" height="30" viewBox="0 0 22 30"><path d="M11 0C5 0 0 5 0 11c0 8 11 19 11 19s11-11 11-19C22 5 17 0 11 0z" fill="#fff"/><circle cx="11" cy="11" r="4" fill="#1e6aa8"/></svg></div>
    <h3>MAIN OFFICE</h3>
    <p>Corvane Power Holdings,<br>Meridian House, Orchard Lane,<br>Tel Aviv 61000 Israel</p>
  </div>
  <div class="contact abs" style="left:359px">
    <div class="ring"><svg width="28" height="20" viewBox="0 0 28 20"><rect width="28" height="20" rx="2" fill="#fff"/><path d="M1 2l13 9 13-9" stroke="#0f3b2e" stroke-width="2" fill="none"/></svg></div>
    <h3>EMAIL</h3>
    <p>info@corvanefund.example</p>
  </div>
  <div class="contact abs" style="left:618px">
    <div class="ring"><svg width="26" height="26" viewBox="0 0 24 24"><path d="M6.6 10.8a15 15 0 0 0 6.6 6.6l2.2-2.2a1 1 0 0 1 1-.25 11 11 0 0 0 3.6.57 1 1 0 0 1 1 1V20a1 1 0 0 1-1 1A17 17 0 0 1 3 4a1 1 0 0 1 1-1h3.5a1 1 0 0 1 1 1c0 1.25.2 2.45.57 3.57a1 1 0 0 1-.25 1z" fill="#fff"/></svg></div>
    <h3>ISRAEL</h3>
    <p>+972-3-555-0148</p>
  </div>
  <div class="contact abs" style="left:877px">
    <div class="ring"><svg width="26" height="26" viewBox="0 0 24 24"><path d="M6.6 10.8a15 15 0 0 0 6.6 6.6l2.2-2.2a1 1 0 0 1 1-.25 11 11 0 0 0 3.6.57 1 1 0 0 1 1 1V20a1 1 0 0 1-1 1A17 17 0 0 1 3 4a1 1 0 0 1 1-1h3.5a1 1 0 0 1 1 1c0 1.25.2 2.45.57 3.57a1 1 0 0 1-.25 1z" fill="#fff"/></svg></div>
    <h3>EUROPE</h3>
    <p>+44 (0) 20 5550 0192</p>
  </div>
  <div class="foot-bar abs">
    <div class="studio"><i></i><span>Northbeam Studio</span></div>
    <div class="legal">Copyrights © 2020, Corvane Power Holdings. . All rights reserved &nbsp;|&nbsp; Privacy Policy &nbsp;|&nbsp; Terms of use</div>
    <div class="to-top"><span>To Top</span><i><svg width="16" height="16" viewBox="0 0 16 16"><path d="M8 14V3M3 8l5-5 5 5" stroke="#fff" stroke-width="2.5" fill="none"/></svg></i></div>
  </div>
</footer>

</body>
</html>
```